Dalvorn-Ke Photography needs a poster for a upcoming event

We need a Music Concert Poster designed for a musician named Marc T. Lindow. The concert is happening 6:30 pm, Saturday, January 10, 2015 Look to our current design ideas for inspiration. Keep it clean and simple but I want to see your creative ideas. Please view the throw togethers screenshots I have included in this project and then use one of the clean images in your design. Visit www.pinboardia.example/marclind/concert-posters/ for the musicians favorite music posters and gather ideas from there as well.

Industry/Entity Type

Event

Requirements
Nice to have
• Lets tend to lean towards a more sanserif font

```html
<!DOCTYPE html>
<html lang="en">
<head>
<meta charset="utf-8">
<title>Marc T. Lindow in Concert</title>
<link href="https://fonts.googleapis.com/css2?family=Oswald:wght@500;600&family=Josefin+Sans:wght@300&family=Encode+Sans+Condensed:wght@300;700&display=swap" rel="stylesheet">
<style>
  :root {
    --paper: #ffffff;
    --frame: #b9b9b9;
    --gold: #b59b3c;
    --gold-soft: rgba(181, 155, 60, 0.55);
    --ink: #2e2b2b;
    --ink-soft: #3d3838;
    --mist: rgba(140, 140, 145, 0.45);
    --glow: rgba(244, 196, 178, 0.55);
    --shirt: #6b2f86;
    --shirt-deep: #3d1d4c;
    --skin: #b88670;
    --hair: #4a3a32;
  }
  * { margin: 0; padding: 0; box-sizing: border-box; }
  html, body {
    width: 1200px; height: 746px; overflow: hidden;
    background: var(--paper);
  }
  .poster {
    position: absolute; left: 25px; top: 25px;
    width: 1151px; height: 698px;
    border: 1px solid var(--frame);
    overflow: hidden;
    background:
      radial-gradient(ellipse 260px 200px at 460px 310px, var(--glow), transparent 70%),
      radial-gradient(ellipse 340px 260px at 140px 350px, var(--mist), transparent 72%),
      radial-gradient(ellipse 300px 140px at 300px 90px, rgba(200,200,205,0.35), transparent 70%),
      var(--paper);
  }
  .artist-photo {
    position: absolute; left: 540px; top: 0;
    width: 611px; height: 698px;
    background:
      radial-gradient(ellipse 190px 230px at 230px 260px, var(--skin), transparent 72%),
      radial-gradient(ellipse 200px 120px at 230px 110px, var(--hair), transparent 75%),
      radial-gradient(ellipse 320px 300px at 400px 560px, var(--shirt), transparent 75%),
      linear-gradient(180deg, transparent 40%, var(--shirt-deep) 100%);
    -webkit-mask-image: linear-gradient(90deg, transparent 0%, #000 32%);
    mask-image: linear-gradient(90deg, transparent 0%, #000 32%);
  }
  .copy {
    position: absolute; left: 52px; top: 0; width: 560px; height: 698px;
    text-align: center;
  }
  .ornament {
    position: absolute;
    background: radial-gradient(ellipse at center, var(--gold-soft), transparent 70%);
  }
  .ornament--top { left: 83px; top: 113px; width: 340px; height: 70px; }
  .artist-name {
    position: absolute; left: 0; top: 198px; width: 100%;
    font-family: "Oswald", sans-serif; font-weight: 600;
    font-size: 68px; line-height: 1; letter-spacing: 2px;
    white-space: nowrap;
    color: var(--gold);
    text-shadow: 0 0 3px #fff, 0 0 6px #fff;
  }
  .event-label {
    position: absolute; left: 0; top: 300px; width: 100%;
    font-family: "Josefin Sans", sans-serif; font-weight: 300;
    font-size: 34px; line-height: 1; letter-spacing: 28px; padding-left: 28px;
    white-space: nowrap;
    color: var(--ink);
  }
  .divider { position: absolute; left: 51px; top: 361px; width: 402px; height: 36px; }
  .divider .ornament { left: 161px; top: 0; width: 80px; height: 36px; }
  .details {
    position: absolute; left: 0; width: 100%;
    font-family: "Encode Sans Condensed", sans-serif; font-weight: 300;
    font-size: 24px; line-height: 34px; color: var(--ink-soft);
    white-space: nowrap;
  }
  .details--date { top: 453px; }
  .details--venue { top: 523px; }
  .admission {
    position: absolute; left: 0; top: 626px; width: 100%;
    font-family: "Encode Sans Condensed", sans-serif; font-weight: 700;
    font-size: 23px; line-height: 28px; letter-spacing: 1px; color: var(--gold);
  }
</style>
</head>
<body>
<main class="poster">
  <div class="artist-photo" role="img" aria-label="Portrait of the musician in a purple shirt, smiling over his shoulder with a guitar"></div>
  <section class="copy">
    <div class="ornament ornament--top" role="img" aria-label="Gold scroll flourish"></div>
    <h1 class="artist-name">MARC T.LINDOW</h1>
    <p class="event-label">IN CONCERT</p>
    <div class="divider">
      <svg width="402" height="36" viewBox="0 0 402 36">
        <line x1="0" y1="18" x2="402" y2="18" stroke="#b59b3c" stroke-width="2"/>
        <circle cx="72" cy="18" r="3" fill="#b59b3c"/>
        <circle cx="330" cy="18" r="3" fill="#b59b3c"/>
      </svg>
      <div class="ornament" role="img" aria-label="Gold centre flourish"></div>
    </div>
    <p class="details details--date">January 10, 2015, Saturday,&nbsp; 6:30 pm</p>
    <p class="details details--venue">Larkmoor Bay SDA Church,<br>240 Harlow Crest Ave.,Larkmoor Bay, FL- 32591</p>
    <p class="admission">FREE ENTRY</p>
  </section>
</main>
</body>
</html>
```